BRAMLEIGH real estate family office

Hello, Our business is a real estate intermediation activity on high-end goods (amounts exceeding € 10m) for corporate and private clients. You can see our logo on the site www.bramleigh-estates.fr We would like to keep that spirit with the hexagon that represents France (transactions between Monaco and Saint Tropez, Courchevel and Paris). And the "baseline" that is "real estate family office". The corporate logo should be and can be printed by embossing (relief). We must integrate the name, first name, phone, email and website. Finally, to imbibe the spirit of business, here is a detail of the activity. "Genuine consulting firm in real estate investments, BRAMLEIGH works with its customers as a specialized player in the high-end markets, we are recognized for our ultra-confidential approach and tailor-made, as well as the quality of our network. We broadcast any information on the market and we work exclusively through a strong relationship we have developed over the years. BRAMLEIGH is active on the French Riviera (from Monaco to Saint-Tropez), the Alps (Courchevel, Méribel, Megève) and Paris (essentially market premium). Always looking for opportunities for our clients, we work on two investment areas: residential luxury real estate (properties, vineyards, mansions, land, etc.) commercial real estate (empty office buildings or yield, hotel properties, land, etc.) "

Target Market(s)

High foreign end customers. corporate and private.

Industry/Entity Type

Real Estate

Contact Information for Business Card

LOGO
baseline
Thibault Marchand
+33(0)6.41.57.94.16
tm@bramleigh-estates.fr
www.bramleigh-estates.fr

Font styles to use
Serif

Colors
cedeed
0255a3
3277b5
85abd2
85cae6
34a7d7
0792cd
cfdeed
1b1b1b

Requirements
Must have
• see description

```html
<!DOCTYPE html>
<html lang="en">
<head>
<meta charset="utf-8">
<title>Bramleigh business card</title>
<link rel="stylesheet" href="https://fonts.googleapis.com/css2?family=Josefin+Sans:wght@300;400&family=Open+Sans:wght@400;600&display=swap">
<style>
  :root {
    --stage: #151515;
    --card-light: #1d62cc;
    --card-mid: #0f4db4;
    --card-dark: #073a97;
    --ink: #ffffff;
    --ink-soft: #cfdeed;
  }
  * { margin: 0; padding: 0; box-sizing: border-box; }
  html, body { width: 1200px; height: 900px; overflow: hidden; }
  body { background: var(--stage); position: relative; }

  .card {
    position: absolute;
    top: 184px;
    height: 491px;
    background: radial-gradient(ellipse 70% 60% at 50% 48%, var(--card-light) 0%, var(--card-mid) 55%, var(--card-dark) 100%);
    color: var(--ink);
  }
  .card--front { left: 314px; width: 301px; }
  .card--back  { left: 645px; width: 304px; }

  .wordmark {
    position: absolute;
    left: 0; right: 0;
    text-align: center;
  }
  .wordmark__name {
    display: block;
    font-family: "Josefin Sans", sans-serif;
    font-weight: 300;
    font-size: 33px;
    letter-spacing: 3px;
    line-height: 1;
  }
  .wordmark__baseline {
    display: block;
    font-family: "Josefin Sans", sans-serif;
    font-weight: 300;
    font-size: 12.5px;
    letter-spacing: 0.6px;
    text-align: right;
    padding-right: 30px;
    margin-top: 8px;
  }
  .card--front .wordmark { top: 102px; }
  .card--back .wordmark { top: 340px; }

  .holder {
    position: absolute;
    left: 0; right: 0;
    top: 284px;
    text-align: center;
    font-family: "Open Sans", sans-serif;
  }
  .holder__name { font-weight: 600; font-size: 19px; letter-spacing: -0.2px; }
  .holder__role { font-weight: 400; font-size: 14.5px; margin-top: 6px; }

  .contact {
    position: absolute;
    left: 0; right: 0;
    top: 372px;
    list-style: none;
    text-align: center;
    font-family: "Open Sans", sans-serif;
    font-size: 15.5px;
    line-height: 23px;
  }
</style>
</head>
<body>
  <section class="card card--front">
    <div class="wordmark">
      <span class="wordmark__name">BRAMLEIGH</span>
      <span class="wordmark__baseline">real estate family office</span>
    </div>
    <div class="holder">
      <p class="holder__name">Thibault Marchand</p>
      <p class="holder__role">CEO</p>
    </div>
    <ul class="contact">
      <li>+33(0)6.41.57.94.16</li>
      <li>tm@bramleigh-estates.fr</li>
      <li>www.bramleigh-estates.fr</li>
    </ul>
  </section>

  <section class="card card--back">
    <div class="wordmark">
      <span class="wordmark__name">BRAMLEIGH</span>
      <span class="wordmark__baseline">real estate family office</span>
    </div>
  </section>
</body>
</html>
```